Corporate Design für junge Steuerberater
Zielgruppe
Wir sind eine junge Steuerberatungsgesellschaft (2 jünge Mütter). Unsere Kunden sind überwiegend kleine Unternehmer
Aufgabenstellung
Logo und Geschäftspapiere sollen leger, aber seriös wirken.
Wir benötigen ein Logo, Visitenkarten, Briefpapier bzw. Deckblätter für unsere Bilanzen, Steuererklärungen. Deckblätter und Briefpapier können auch gleich aussehen.
(Das Beispielbild ist natürlich nicht von unserem Unternehmen, würde uns vom Stil her gut gefallen....ist aber kein Muss)

```html
<!DOCTYPE html>
<html lang="de">
<head>
<meta charset="utf-8">
<title>KTR Steuerberatung GesmbH – Briefpapier</title>
<link href="https://fonts.googleapis.com/css2?family=Montserrat:wght@500;600;700&display=swap" rel="stylesheet">
<style>
  :root {
    --backdrop: #ecebe8;
    --paper: #ffffff;
    --ink: #343c44;
    --accent: #4dbb8c;
    --watermark: #e7e8ea;
    --rule: #4a5057;
  }
  * { margin: 0; padding: 0; box-sizing: border-box; }
  html, body {
    width: 1200px;
    height: 1189px;
    overflow: hidden;
    background: var(--backdrop);
    font-family: "Montserrat", sans-serif;
  }
  .stationery {
    position: relative;
    width: 1200px;
    height: 1189px;
  }
  .letterhead {
    position: absolute;
    width: 544px;
    height: 769px;
    background: var(--paper);
    overflow: hidden;
    box-shadow: 0 4px 14px rgba(0, 0, 0, 0.22);
  }
  .letterhead--front { left: 87px; top: 112px; z-index: 2; }
  .letterhead--back  { left: 549px; top: 283px; z-index: 1; }

  .letterhead__bar {
    position: absolute;
    left: 0;
    bottom: 0;
    width: 16px;
    background: var(--accent);
  }
  .letterhead--front .letterhead__bar { top: 216px; }
  .letterhead--back .letterhead__bar { top: 598px; }

  .brand {
    position: absolute;
    text-align: center;
    color: var(--ink);
  }
  .letterhead--front .brand { left: 50px; top: 62px; width: 180px; }
  .letterhead--back .brand { left: 162px; top: 44px; width: 232px; }

  .brand__name {
    display: block;
    font-weight: 700;
    font-size: 40px;
    letter-spacing: 1px;
    line-height: 1;
  }
  .letterhead--back .brand__name { font-size: 52px; }

  .brand__line {
    display: flex;
    align-items: center;
    justify-content: center;
    gap: 8px;
    margin-top: 10px;
    font-weight: 600;
    font-size: 11px;
    letter-spacing: 0.5px;
    color: var(--ink);
  }
  .letterhead--back .brand__line { font-size: 14px; margin-top: 14px; }
  .brand__line::before,
  .brand__line::after {
    content: "";
    width: 22px;
    height: 1px;
    background: var(--rule);
  }
  .letterhead--back .brand__line::before,
  .letterhead--back .brand__line::after { width: 30px; }

  .letterhead__watermark {
    position: absolute;
    left: 28px;
    bottom: -42px;
    font-weight: 600;
    font-size: 205px;
    letter-spacing: 6px;
    line-height: 1;
    color: var(--watermark);
    white-space: nowrap;
  }
</style>
</head>
<body>
  <main class="stationery">
    <section class="letterhead letterhead--front">
      <div class="letterhead__bar"></div>
      <header class="brand">
        <span class="brand__name">KTR</span>
        <span class="brand__line">Steuerberatung GesmbH</span>
      </header>
      <div class="letterhead__watermark" aria-hidden="true">KTR</div>
    </section>

    <section class="letterhead letterhead--back">
      <div class="letterhead__bar"></div>
      <header class="brand">
        <span class="brand__name">KTR</span>
        <span class="brand__line">Steuerberatung GesmbH</span>
      </header>
      <div class="letterhead__watermark" aria-hidden="true">KTR</div>
    </section>
  </main>
</body>
</html>
```